Design a modern, classy & professional business card for an online real estate agency, specializing in medium-luxury properties in Thailand and later in Singapore and UK.

Possible design ideas so far: (not essential)

- curved corner(s) to the card, white on front & turquoise on back or visa versa.

- front of card - clear and simple, company name in metallic grey/monochrome, logo graphic & company name on front in spot UV or embossed/debossed effect.

- back of card - large, close-cropped, 'ghost' patterns of the C-shaped curves of logo, or company name repeated on back of card in spot UV.

Target Market(s)

- young to middle-aged professionals mainly (but ideally should design should suit all)

- UK, US,EU,AUS & ASIAN mainly (but ideally should design should suit all countries)

Industry/Entity Type

Real Estate

Requirements
Must have
• THEME:
- Luxurious & Modern
- Clean & striking
- Unique & creative

INFO:
- Logo & company name on front
- Contact details on back:

Tobias Lindqvar
Managing Director

www.velmoraestates.example
www.velmoraestates-uk.example

Tel: 084-273-6190
email: tobias@velmoraestates.example

(contact details can be displayed in any order as suites design.)

Nice to have
• - curved corner(s) to the card, white on front & turquoise on back or visa versa.

Should not have
• - No generic images of properties, palm trees/coconut trees etc.

- No other other bold colors, except for main turquoise, grey, metallic white & black theme.

- No obvious business card templates

```html
<!DOCTYPE html>
<html lang="en">
<head>
<meta charset="utf-8">
<title>Velmora Estates – Business Card</title>
<link rel="stylesheet" href="https://fonts.googleapis.com/css2?family=Arimo:wght@400&family=Marcellus&family=Varela+Round&display=swap">
<style>
  :root {
    --backdrop: #e9ecec;
    --card-white: #ffffff;
    --mint: #7fe3c4;
    --mint-light: #b3f2dd;
    --mint-deep: #6fd3b4;
    --grey: #6b7371;
    --ink: #2f3534;
    --shadow: rgba(0, 0, 0, 0.22);
  }
  * { box-sizing: border-box; margin: 0; padding: 0; }
  html, body {
    width: 1200px; height: 820px; overflow: hidden;
    background: var(--backdrop);
  }
  .stage { position: relative; width: 1200px; height: 820px; }

  .card {
    position: absolute;
    width: 560px; height: 330px;
    background: var(--card-white);
    border-radius: 26px;
    overflow: hidden;
    box-shadow: 0 14px 30px var(--shadow);
  }

  /* Front */
  .card--front { left: 30px; top: 100px; }
  .holder { position: absolute; right: 34px; top: 28px; text-align: right; }
  .holder__name {
    font-family: "Arimo", sans-serif;
    font-size: 28px; color: var(--ink); letter-spacing: 0.5px;
  }
  .holder__title {
    font-family: "Arimo", sans-serif;
    font-size: 11px; color: var(--grey); margin-top: 2px;
  }
  .brand { position: absolute; left: 70px; top: 118px; display: flex; align-items: center; gap: 24px; }
  .brand__square { width: 150px; height: 142px; background: var(--mint); }
  .brand__name {
    font-family: "Marcellus", serif;
    color: var(--grey); line-height: 1;
  }
  .brand__name-main { display: block; font-size: 74px; }
  .brand__name-sub { display: block; font-size: 30px; letter-spacing: 9px; margin-top: 4px; }

  /* Back */
  .card--back { left: 610px; top: 390px; }
  .cityscape {
    position: absolute; left: 0; top: 0; width: 560px; height: 190px;
    background:
      radial-gradient(circle at 78% 22%, rgba(255,255,255,0.85) 0, rgba(255,255,255,0) 60px),
      linear-gradient(180deg, var(--mint-light) 0%, var(--mint) 60%, var(--mint-deep) 100%);
  }
  .holder--back { top: 202px; right: 30px; }
  .holder--back .holder__name { font-size: 25px; }
  .contacts {
    position: absolute; left: 42px; top: 252px;
    list-style: none;
    font-family: "Varela Round", sans-serif;
    font-size: 12px; color: var(--ink);
  }
  .contacts li { display: flex; align-items: center; gap: 8px; height: 16px; }
  .contacts svg { width: 11px; height: 11px; flex: none; }
</style>
</head>
<body>
<main class="stage">

  <section class="card card--front" aria-label="Card front">
    <div class="holder">
      <p class="holder__name">Tobias Lindqvar</p>
      <p class="holder__title">Managing Director</p>
    </div>
    <div class="brand">
      <div class="brand__square"></div>
      <p class="brand__name">
        <span class="brand__name-main">Velmora</span>
        <span class="brand__name-sub">ESTATES</span>
      </p>
    </div>
  </section>

  <section class="card card--back" aria-label="Card back">
    <div class="cityscape" role="img" aria-label="Illustrated city skyline of tall buildings and small trees under a soft glowing sky"></div>
    <div class="holder holder--back">
      <p class="holder__name">Tobias Lindqvar</p>
      <p class="holder__title">Managing Director</p>
    </div>
    <ul class="contacts">
      <li>
        <svg viewBox="0 0 12 12" aria-hidden="true"><circle cx="6" cy="6" r="5" fill="none" stroke="currentColor" stroke-width="1.3"/><path d="M1 6h10M6 1c-2.5 3-2.5 7 0 10M6 1c2.5 3 2.5 7 0 10" fill="none" stroke="currentColor" stroke-width="1"/></svg>
        www.velmoraestates.example
      </li>
      <li>
        <svg viewBox="0 0 12 12" aria-hidden="true"><circle cx="6" cy="6" r="5" fill="none" stroke="currentColor" stroke-width="1.3"/><path d="M1 6h10M6 1c-2.5 3-2.5 7 0 10M6 1c2.5 3 2.5 7 0 10" fill="none" stroke="currentColor" stroke-width="1"/></svg>
        www.velmoraestates-uk.example
      </li>
      <li>
        <svg viewBox="0 0 12 12" aria-hidden="true"><path d="M1 4c0-2 10-2 10 0v1H8V4H4v1H1z M3 5h6l2 5H1z" fill="currentColor"/></svg>
        Tel: 084-273-6190
      </li>
      <li>
        <svg viewBox="0 0 12 12" aria-hidden="true"><rect x="1" y="2.5" width="10" height="7" fill="none" stroke="currentColor" stroke-width="1.2"/><path d="M1 2.5l5 4 5-4" fill="none" stroke="currentColor" stroke-width="1.2"/></svg>
        email: tobias@velmoraestates.example
      </li>
    </ul>
  </section>

</main>
</body>
</html>
```